Landscape design build company door flyer

I would like this flyer to convey a high-level of professionalism for a company that is excellent with communication with their clients as well as a company that does incredible installations

Went on vacation/holiday

```html
<!DOCTYPE html>
<html lang="en">
<head>
<meta charset="utf-8">
<title>Lotus Landworks – Outdoor Living Flyer</title>
<link href="https://fonts.googleapis.com/css2?family=Montserrat:wght@500;600;700;800;900&family=Open+Sans:wght@400;600;700&display=swap" rel="stylesheet">
<style>
  :root{
    --ink:#1f1f1f;
    --charcoal:#2a2a2a;
    --charcoal-deep:#1b1b1b;
    --yellow:#f6b70f;
    --white:#ffffff;
    --muted:#cfcfcf;
  }
  *{box-sizing:border-box;margin:0;padding:0}
  html,body{width:849px;height:1200px;overflow:hidden;background:var(--charcoal)}
  .flyer{position:relative;width:849px;height:1200px;font-family:'Open Sans',sans-serif;color:var(--white);overflow:hidden;background:var(--charcoal)}

  /* hero */
  .hero{position:absolute;left:0;top:0;width:849px;height:400px}
  .hero-photo{position:absolute;inset:0;background:linear-gradient(160deg,#6d6a5e 0%,#4a4a40 35%,#3b3d33 60%,#2f302c 100%)}
  .hero-shade{position:absolute;inset:0;background:linear-gradient(180deg,rgba(0,0,0,.15) 0%,rgba(0,0,0,.35) 55%,rgba(30,30,30,.95) 100%)}
  .brand{position:absolute;left:50%;top:30px;transform:translateX(-50%);width:250px;height:126px;background:var(--white);display:flex;flex-direction:column;align-items:center;justify-content:center;gap:6px}
  .brand-mark{width:40px;height:40px;border-radius:50%;background:var(--charcoal)}
  .brand-name{font-family:'Montserrat',sans-serif;font-weight:800;font-size:21px;color:var(--charcoal);letter-spacing:.5px;text-transform:uppercase}
  .brand-tag{font-family:'Montserrat',sans-serif;font-weight:600;font-size:9px;color:var(--charcoal);letter-spacing:1.5px;text-transform:uppercase;margin-top:-4px}
  .headline{position:absolute;left:0;right:0;top:232px;text-align:center;font-family:'Montserrat',sans-serif;font-weight:900;font-size:55px;line-height:1;text-transform:uppercase}
  .headline span{display:block}
  .headline .accent{color:var(--yellow)}
  .hero-sub{position:absolute;left:0;right:0;top:352px;text-align:center;font-weight:700;font-size:19px}

  /* services grid */
  .services{position:absolute;left:0;top:400px;width:849px;height:480px;background:var(--charcoal)}
  .pill{position:absolute;left:50%;transform:translateX(-50%);font-family:'Montserrat',sans-serif;font-weight:800;text-transform:uppercase;white-space:nowrap}
  .services .pill{top:8px;background:var(--white);color:var(--charcoal);font-size:23px;padding:6px 26px;border-radius:6px}
  .grid{position:absolute;left:92px;top:58px;display:grid;grid-template-columns:repeat(3,208px);column-gap:18px;row-gap:16px}
  .card{width:208px;height:195px;border-radius:12px;overflow:hidden;background:var(--charcoal-deep);display:flex;flex-direction:column}
  .card-photo{flex:1}
  .card-label{height:36px;display:flex;align-items:center;justify-content:center;font-family:'Montserrat',sans-serif;font-weight:800;font-size:14px;text-transform:uppercase}
  .p1{background:linear-gradient(150deg,#8b8a7e,#5d5a4c)}
  .p2{background:linear-gradient(150deg,#8a6a4a,#5b3e26)}
  .p3{background:linear-gradient(150deg,#7d8a6a,#6b6a62)}
  .p4{background:linear-gradient(150deg,#6f5a44,#7c3c2c)}
  .p5{background:linear-gradient(150deg,#c9d6de,#3f8fb8)}
  .p6{background:linear-gradient(150deg,#8f8a80,#5b5a52)}

  /* list band */
  .provide{position:absolute;left:0;top:868px;width:849px;height:232px;background:var(--yellow);color:var(--ink)}
  .provide .pill{top:-14px;background:var(--charcoal);color:var(--white);font-size:19px;padding:7px 24px;border-radius:6px}
  .provide-cols{position:absolute;left:50px;top:42px;display:grid;grid-template-columns:170px 170px 190px 180px;column-gap:14px}
  .provide-cols ul{list-style:none}
  .provide-cols li{display:flex;align-items:flex-start;gap:8px;font-size:13.5px;font-weight:600;line-height:1.25;margin-bottom:10px}
  .tick{flex:0 0 17px;width:17px;height:17px;margin-top:1px}

  /* footer */
  .footer{position:absolute;left:0;top:1100px;width:849px;height:100px;background:var(--charcoal-deep);display:flex;align-items:center;padding:0 50px}
  .contact{display:flex;align-items:center;gap:14px}
  .contact svg{width:34px;height:34px}
  .call-label{font-size:14px;color:var(--muted)}
  .call-number{font-family:'Montserrat',sans-serif;font-weight:800;font-size:24px}
  .divider{width:2px;height:54px;background:#555;margin:0 28px}
  .address{font-size:14px;line-height:1.35}
  .address .web{color:var(--muted);font-size:12px}
  .cta{margin-left:auto;background:var(--yellow);color:var(--ink);font-family:'Montserrat',sans-serif;font-weight:800;font-size:15px;padding:12px 20px;text-transform:uppercase;border-radius:3px}
</style>
</head>
<body>
<main class="flyer">

  <header class="hero">
    <div class="hero-photo" role="img" aria-label="Photo of a finished backyard with fence, lawn and patio"></div>
    <div class="hero-shade"></div>
    <div class="brand">
      <div class="brand-mark"></div>
      <div class="brand-name">Lotus Landworks</div>
      <div class="brand-tag">Outdoor Living Spaces</div>
    </div>
    <h1 class="headline"><span>It's Time To</span><span class="accent">Discover Your Zen</span></h1>
    <p class="hero-sub">From vision to reality, let us bring your dream outdoor space to life.</p>
  </header>

  <section class="services">
    <h2 class="pill">Our Services</h2>
    <div class="grid">
      <div class="card"><div class="card-photo p1" role="img" aria-label="Photo of a paver patio with pergola"></div><div class="card-label">Paver Patios</div></div>
      <div class="card"><div class="card-photo p2" role="img" aria-label="Photo of a paver driveway in front of wooden garage doors"></div><div class="card-label">Paver Driveways</div></div>
      <div class="card"><div class="card-photo p3" role="img" aria-label="Photo of stone retaining walls and steps"></div><div class="card-label">Retaining Walls</div></div>
      <div class="card"><div class="card-photo p4" role="img" aria-label="Photo of a wooden deck with railings and seating"></div><div class="card-label">Decks &amp; Railings</div></div>
      <div class="card"><div class="card-photo p5" role="img" aria-label="Photo of a backyard swimming pool"></div><div class="card-label">Pools</div></div>
      <div class="card"><div class="card-photo p6" role="img" aria-label="Photo of an outdoor stone fireplace"></div><div class="card-label">Firepits &amp; Fireplaces</div></div>
    </div>
  </section>

  <section class="provide">
    <h2 class="pill">Some of the services we provide:</h2>
    <div class="provide-cols">
      <ul>
        <li><svg class="tick" viewBox="0 0 20 20"><rect width="20" height="20" rx="3" fill="#2a2a2a"/><path d="M5 10.5l3.2 3.2L15 6.8" stroke="#f6b70f" stroke-width="2.4" fill="none"/></svg>Landscape design</li>
        <li><svg class="tick" viewBox="0 0 20 20"><rect width="20" height="20" rx="3" fill="#2a2a2a"/><path d="M5 10.5l3.2 3.2L15 6.8" stroke="#f6b70f" stroke-width="2.4" fill="none"/></svg>Landscaping</li>
        <li><svg class="tick" viewBox="0 0 20 20"><rect width="20" height="20" rx="3" fill="#2a2a2a"/><path d="M5 10.5l3.2 3.2L15 6.8" stroke="#f6b70f" stroke-width="2.4" fill="none"/></svg>Hardscaping</li>
        <li><svg class="tick" viewBox="0 0 20 20"><rect width="20" height="20" rx="3" fill="#2a2a2a"/><path d="M5 10.5l3.2 3.2L15 6.8" stroke="#f6b70f" stroke-width="2.4" fill="none"/></svg>Retaining wall design</li>
        <li><svg class="tick" viewBox="0 0 20 20"><rect width="20" height="20" rx="3" fill="#2a2a2a"/><path d="M5 10.5l3.2 3.2L15 6.8" stroke="#f6b70f" stroke-width="2.4" fill="none"/></svg>Retaining walls</li>
      </ul>
      <ul>
        <li><svg class="tick" viewBox="0 0 20 20"><rect width="20" height="20" rx="3" fill="#2a2a2a"/><path d="M5 10.5l3.2 3.2L15 6.8" stroke="#f6b70f" stroke-width="2.4" fill="none"/></svg>Pool designs</li>
        <li><svg class="tick" viewBox="0 0 20 20"><rect width="20" height="20" rx="3" fill="#2a2a2a"/><path d="M5 10.5l3.2 3.2L15 6.8" stroke="#f6b70f" stroke-width="2.4" fill="none"/></svg>Driveways</li>
        <li><svg class="tick" viewBox="0 0 20 20"><rect width="20" height="20" rx="3" fill="#2a2a2a"/><path d="M5 10.5l3.2 3.2L15 6.8" stroke="#f6b70f" stroke-width="2.4" fill="none"/></svg>Firepits</li>
        <li><svg class="tick" viewBox="0 0 20 20"><rect width="20" height="20" rx="3" fill="#2a2a2a"/><path d="M5 10.5l3.2 3.2L15 6.8" stroke="#f6b70f" stroke-width="2.4" fill="none"/></svg>Pavers</li>
        <li><svg class="tick" viewBox="0 0 20 20"><rect width="20" height="20" rx="3" fill="#2a2a2a"/><path d="M5 10.5l3.2 3.2L15 6.8" stroke="#f6b70f" stroke-width="2.4" fill="none"/></svg>Deck designs</li>
      </ul>
      <ul>
        <li><svg class="tick" viewBox="0 0 20 20"><rect width="20" height="20" rx="3" fill="#2a2a2a"/><path d="M5 10.5l3.2 3.2L15 6.8" stroke="#f6b70f" stroke-width="2.4" fill="none"/></svg>Luxury outdoor renovations</li>
        <li><svg class="tick" viewBox="0 0 20 20"><rect width="20" height="20" rx="3" fill="#2a2a2a"/><path d="M5 10.5l3.2 3.2L15 6.8" stroke="#f6b70f" stroke-width="2.4" fill="none"/></svg>Outdoor living spaces</li>
        <li><svg class="tick" viewBox="0 0 20 20"><rect width="20" height="20" rx="3" fill="#2a2a2a"/><path d="M5 10.5l3.2 3.2L15 6.8" stroke="#f6b70f" stroke-width="2.4" fill="none"/></svg>Patio designs</li>
        <li><svg class="tick" viewBox="0 0 20 20"><rect width="20" height="20" rx="3" fill="#2a2a2a"/><path d="M5 10.5l3.2 3.2L15 6.8" stroke="#f6b70f" stroke-width="2.4" fill="none"/></svg>Outdoor lighting</li>
      </ul>
      <ul>
        <li><svg class="tick" viewBox="0 0 20 20"><rect width="20" height="20" rx="3" fill="#2a2a2a"/><path d="M5 10.5l3.2 3.2L15 6.8" stroke="#f6b70f" stroke-width="2.4" fill="none"/></svg>Outdoor kitchen spaces</li>
        <li><svg class="tick" viewBox="0 0 20 20"><rect width="20" height="20" rx="3" fill="#2a2a2a"/><path d="M5 10.5l3.2 3.2L15 6.8" stroke="#f6b70f" stroke-width="2.4" fill="none"/></svg>Fencing</li>
        <li><svg class="tick" viewBox="0 0 20 20"><rect width="20" height="20" rx="3" fill="#2a2a2a"/><path d="M5 10.5l3.2 3.2L15 6.8" stroke="#f6b70f" stroke-width="2.4" fill="none"/></svg>Fireplaces</li>
        <li><svg class="tick" viewBox="0 0 20 20"><rect width="20" height="20" rx="3" fill="#2a2a2a"/><path d="M5 10.5l3.2 3.2L15 6.8" stroke="#f6b70f" stroke-width="2.4" fill="none"/></svg>Sheds</li>
      </ul>
    </div>
  </section>

  <footer class="footer">
    <div class="contact">
      <svg viewBox="0 0 24 24" aria-hidden="true"><path d="M6.6 10.8a15.1 15.1 0 0 0 6.6 6.6l2.2-2.2a1 1 0 0 1 1-.25 11.4 11.4 0 0 0 3.6.57 1 1 0 0 1 1 1V20a1 1 0 0 1-1 1A17 17 0 0 1 3 4a1 1 0 0 1 1-1h3.5a1 1 0 0 1 1 1c0 1.25.2 2.45.57 3.57a1 1 0 0 1-.25 1z" fill="#f6b70f"/></svg>
      <div>
        <div class="call-label">Call Us Now!</div>
        <div class="call-number">(206) 555-0148</div>
      </div>
    </div>
    <div class="divider"></div>
    <div class="contact">
      <svg viewBox="0 0 24 24" aria-hidden="true"><path d="M12 2a7 7 0 0 0-7 7c0 5.2 7 13 7 13s7-7.8 7-13a7 7 0 0 0-7-7zm0 9.5A2.5 2.5 0 1 1 12 6.5a2.5 2.5 0 0 1 0 5z" fill="#f6b70f"/></svg>
      <div class="address">1820 NE Cedar Lane<br>Redmond, WA 98052<br><span class="web">www.lotuslandworks.com</span></div>
    </div>
    <div class="cta">Get a Free Estimate</div>
  </footer>

</main>
</body>
</html>
```